Aviation: Overcast Study Guide Book Cover

We need a book cover (front and back) designed for an Instrument Flight Rules (IFR) study guide used by helicopter and airplane pilots to obtain an instrument rating for a helicopter or airplane. Below is the title and subtitles.

TITLE: OVERCAST STUDY GUIDE
SUBTITLE 1: Checkride Preparation for Airplane and Helicopter Pilots
SUBTITLE 2: Prepare for your Instrument Rating with Confidence

We have also upload recommended text to be included on the back cover. In addition, we included images of similar book covers that we like and ones that we do not like. Below are links to two others books by the author.

https://www.bookvarro.example/Rotorcraft-Exam-Handbook-oral-review/dp/507214638K
https://www.bookvarro.example/Manual-Floatwing-Handling-Lionel-Quarrick/dp/5093742816

Flight students

Aviation

• helicopter and airplane

```html
<!DOCTYPE html>
<html lang="en">
<head>
<meta charset="utf-8">
<title>Overcast Study Guide – Cover Spread</title>
<link href="https://fonts.googleapis.com/css2?family=Bebas+Neue&family=Lato:wght@300;400;700;900&display=swap" rel="stylesheet">
<style>
  :root {
    --stage: #111111;
    --sky-top: #2f86c9;
    --sky-mid: #4f9fd8;
    --sky-low: #cfe4f4;
    --cloud: #f7fafd;
    --panel: rgba(0, 84, 170, 0.78);
    --panel-low: rgba(0, 124, 200, 0.8);
    --accent: #0a8fd4;
    --white: #ffffff;
    --ink: #111418;
    --spine-line: rgba(40, 60, 80, 0.45);
  }
  * { margin: 0; padding: 0; box-sizing: border-box; }
  html, body { width: 1200px; height: 1200px; overflow: hidden; background: var(--stage); }
  body { position: relative; font-family: 'Lato', sans-serif; color: var(--white); }

  .cover-spread {
    position: absolute; left: 87px; top: 274px; width: 1027px; height: 651px;
    overflow: hidden;
  }
  .sky-chart {
    position: absolute; inset: 0;
    background: linear-gradient(180deg, var(--sky-top) 0%, var(--sky-mid) 45%, var(--sky-low) 80%, var(--cloud) 100%);
  }
  .spine-fold { position: absolute; top: 0; bottom: 0; width: 1px; background: var(--spine-line); }
  .spine-fold.left { left: 502px; }
  .spine-fold.right { left: 524px; }

  /* Back cover */
  .back-panel {
    position: absolute; left: 30px; top: 38px; width: 444px; height: 482px;
    background: linear-gradient(180deg, var(--panel) 0%, var(--panel-low) 100%);
    padding: 14px 13px 0;
  }
  .back-heading {
    font-weight: 700; font-size: 18.5px; line-height: 23px; text-align: center;
    letter-spacing: 0.3px; text-transform: uppercase;
  }
  .back-sub {
    font-weight: 700; font-size: 12.5px; text-align: center; letter-spacing: 0.4px;
    text-transform: uppercase; margin-top: 27px;
  }
  .back-copy { font-size: 9.3px; line-height: 11.9px; text-align: justify; margin-top: 8px; }
  .back-copy.lead { margin-top: 7px; }
  .topic-grid {
    margin: 19px auto 0; width: 368px; border-collapse: collapse;
    font-size: 9.6px;
  }
  .topic-grid td {
    border: 1.5px solid var(--white); height: 24.5px; text-align: center; width: 33.3%;
  }
  .back-rule { height: 1px; background: var(--white); margin: 34px 4px 0; }
  .author-bio { font-size: 9.3px; line-height: 11.9px; text-align: justify; margin-top: 27px; }
  .author-bio strong { font-size: 12.5px; font-weight: 700; }
  .isbn-box { position: absolute; left: 356px; top: 566px; width: 118px; height: 70px; background: var(--accent); }

  /* Front cover */
  .front-title {
    position: absolute; left: 600px; width: 427px; text-align: center;
    font-family: 'Bebas Neue', sans-serif; color: var(--white);
  }
  .title-main { top: 14px; font-size: 118px; line-height: 200px; letter-spacing: 1px; }
  .title-sub { top: 218px; font-size: 60px; line-height: 60px; letter-spacing: 1px; }
  .front-subtitle {
    position: absolute; left: 580px; width: 467px; top: 304px; text-align: center;
    font-size: 19px; line-height: 22px; letter-spacing: 2.3px; text-transform: uppercase; font-weight: 400;
  }
  .aircraft-photo {
    position: absolute; left: 565px; top: 369px; width: 418px; height: 164px;
    background: radial-gradient(ellipse at 50% 55%, #eef1f4 0%, #c9d6e2 40%, rgba(150,185,215,0) 72%);
  }
  .front-tagline {
    position: absolute; left: 580px; width: 467px; top: 571px; text-align: center;
    font-size: 16.5px; font-weight: 300; color: var(--ink); letter-spacing: 0.4px;
  }
  .front-author {
    position: absolute; left: 580px; width: 467px; top: 598px; text-align: center;
    font-size: 30px; font-weight: 900; color: var(--ink); letter-spacing: 5px; text-transform: uppercase;
  }
</style>
</head>
<body>
  <section class="cover-spread">
    <div class="sky-chart" role="img" aria-label="Blue sky with faint instrument navigation chart lines fading into white clouds"></div>
    <div class="spine-fold left"></div>
    <div class="spine-fold right"></div>

    <div class="back-panel">
      <h2 class="back-heading">Prepare for your IFR check ride<br>with confidence</h2>
      <p class="back-copy lead">Becoming an instrument rated pilot is one of the most challenging ratings to obtain. This guide helps prepare you to pass your IFR check ride with confidence. The question-and-answer format is easy to follow and provides detailed explanations for expanded knowledge.</p>
      <h3 class="back-sub">Includes helicopter and airplane specific content</h3>
      <p class="back-copy">This guide is designed to prepare an airplane or helicopter pilot the oral portion of the IFR checkride. Unlike other resources, this guide specifically addresses the differences with IFR flight in helicopters. As a dual rated pilot, the author ensures to identify areas of differences between the two categories of IFR flight. The following concepts are addressed within the guide</p>
      <table class="topic-grid">
        <tr><td>Preflight Actions</td><td>Enroute Procedures</td><td>Aeromedical Factors</td></tr>
        <tr><td>General IFR Concepts</td><td>Approach Procedures</td><td>Weather Fundamentals</td></tr>
        <tr><td>Departure Procedures</td><td>IFR Emergences</td><td>Risk Management</td></tr>
      </table>
      <div class="back-rule"></div>
      <p class="author-bio"><strong>LIONEL QUARRICK</strong> is ATP rated pilot and helicopter and fixed-wing instructor. Lionel is the owner and operator Crosswind Ridge, LLC which does business as Hoverline Aviation and Pontoon Aviation. Hoverline Aviation provides primary helicopter flight instruction while Pontoon Aviation provides seaplane flight instruction and tours. In addition to instructing, Lionel has authored other books to include Rotorcraft Exam Handbook, and Manual of Floatwing Handling. Lionel lives in Kentucky with his beautiful wife Marla. They have a daughter, Jess, that is dual rated and employed as a captain for a charter company. Prior to learning to fly, Lionel spent several years in the military as a Special Warfare Combat Craft Crewman in the U.S. Navy and Ranger-qualified infantry officer in the U.S. Army.</p>
    </div>
    <div class="isbn-box"></div>

    <h1 class="front-title title-main">OVERCAST</h1>
    <div class="front-title title-sub">STUDY GUIDE</div>
    <p class="front-subtitle">Checkride preparation for<br>airplane and helicopter pilots</p>
    <div class="aircraft-photo" role="img" aria-label="White single-engine turboprop utility airplane flying above the clouds"></div>
    <p class="front-tagline">Prepare for your Instrument Rating with Confidence</p>
    <p class="front-author">Lionel Quarrick</p>
  </section>
</body>
</html>
```